Concise,Good colour matching,Good looks design for "HERD SURE RAPID TEST FOR LIVESTOCK"

Product Positioning: Affordable test for Large Animals (Livestock/Veterinary Use)
Product Name: HERD SURE Rapid Test Kit (for large animals, e.g., cattle, horses, swine,Avian,sheep).

2. Packaging Requirements

A. Visual Design
Color Scheme:
Green/Blue/Orange/Yellow/Red/Gray/White(chose 2~4 colors)

Mandatory Info:
Brand logo ("HERD SURE")

Target Market(s)

Southeast Asia, Africa, Middle East, South America

Industry/Entity Type

Veterinary diagnostic for LIVESTOCK

Colors

Designer to choose colors to be used in the design.

Requirements
Nice to have
• Concise,Good colour matching,Good looks

```html
<!DOCTYPE html>
<html lang="en">
<head>
<meta charset="utf-8">
<title>Herd Sure Rapid Test – Packaging Layout</title>
<link href="https://fonts.googleapis.com/css2?family=Poppins:wght@400;500;600;700&family=Allura&display=swap" rel="stylesheet">
<style>
  :root {
    --navy: #0b3a80;
    --navy-deep: #083171;
    --green: #6cc630;
    --green-bright: #74cf2f;
    --sky: #92dcf2;
    --sky-soft: #d9f3fb;
    --ink: #1a1f36;
    --paper: #ffffff;
    --stage: #f1f1f1;
    --label-gray: #f0f0f0;
  }
  * { margin: 0; padding: 0; box-sizing: border-box; }
  html, body {
    width: 1200px; height: 470px; overflow: hidden;
    background: var(--stage);
    font-family: "Poppins", sans-serif;
    color: var(--ink);
  }
  .layout {
    position: absolute; left: 147px; top: 10px;
    width: 906px; height: 450px;
  }
  .panel {
    position: absolute; background: var(--paper); overflow: hidden;
    box-shadow: 0 2px 8px rgba(0,0,0,0.06);
  }

  /* Front panel */
  .front { left: 0; top: 0; width: 600px; height: 450px; }
  .front .swoosh { position: absolute; left: 0; top: 0; }
  .brand-name {
    position: absolute; left: 33px; top: 52px;
    font-weight: 600; font-size: 27px; color: var(--ink); letter-spacing: -0.5px;
  }
  .headline { position: absolute; left: 32px; top: 132px; line-height: 1; z-index: 2; }
  .headline .line {
    display: block; font-weight: 700; font-size: 42px; letter-spacing: -1.5px;
  }
  .headline .blue { color: var(--navy); }
  .headline .green { color: var(--green); }
  .headline .line + .line { margin-top: -2px; }
  .headline .for-row { display: flex; align-items: baseline; margin-top: 8px; }
  .headline .script {
    font-family: "Allura", cursive; font-size: 56px; color: var(--ink);
    margin-right: 8px; line-height: 0.8;
  }
  .headline .indent { padding-left: 26px; margin-top: 0; }
  .subline {
    position: absolute; left: 33px; top: 362px;
    font-size: 16px; font-weight: 400; line-height: 1.3; color: var(--ink);
  }
  .hero-photo {
    position: absolute; left: 300px; top: 105px; width: 282px; height: 345px;
    background: radial-gradient(ellipse 60% 55% at 62% 45%, #b4582b 0%, #a14b25 55%, #e6d8c7 80%, rgba(255,255,255,0) 100%);
  }

  /* Brand panel */
  .brand-panel {
    left: 610px; top: 0; width: 296px; height: 118px;
    background: var(--navy-deep);
    display: flex; align-items: center; justify-content: center;
  }
  .brand-panel .brand-mark {
    color: var(--paper); font-weight: 600; font-size: 30px; letter-spacing: -0.5px;
  }

  /* Feature panel */
  .features { left: 610px; top: 127px; width: 296px; height: 156px; }
  .features .title {
    position: absolute; left: 17px; top: 14px;
    font-weight: 600; font-size: 13.5px; line-height: 1.05; letter-spacing: -0.3px;
  }
  .features .point {
    position: absolute; font-size: 6.6px; line-height: 1.25; color: var(--ink); z-index: 2;
  }
  .features .point b { font-weight: 600; }
  .features .fast { left: 17px; top: 54px; width: 102px; }
  .features .reliable {
    left: 16px; top: 100px; width: 113px; height: 39px;
    background: var(--sky); padding: 4px 5px;
  }
  .features .goat-photo {
    position: absolute; left: 124px; top: 30px; width: 36px; height: 106px;
    background: linear-gradient(180deg, #ece6df 0%, #d9cfc4 60%, #f3efea 100%);
    border-radius: 16px 16px 8px 8px;
    z-index: 1;
  }
  .features .value-card {
    position: absolute; left: 164px; top: 15px; width: 115px; height: 124px;
    background: var(--green-bright); color: var(--paper); padding: 8px 9px;
  }
  .value-card .value-title { font-weight: 600; font-size: 13px; letter-spacing: -0.3px; }
  .value-card .value-text { font-size: 6.6px; line-height: 1.25; margin-top: 3px; }
  .value-card .value-brand {
    position: absolute; left: 9px; bottom: 7px;
    font-weight: 600; font-size: 16px; color: rgba(255,255,255,0.35);
  }

  /* Info panel */
  .info { left: 610px; top: 292px; width: 296px; height: 158px; }
  .info .label {
    position: absolute; left: 13px; top: 48px; width: 138px; height: 56px;
    background: var(--label-gray); padding: 5px 7px;
    font-size: 7.4px; line-height: 1.35;
  }
  .info .label .label-name { font-weight: 600; font-size: 8.4px; }
</style>
</head>
<body>
  <main class="layout">
    <section class="panel front">
      <svg class="swoosh" width="600" height="450" viewBox="0 0 600 450" aria-hidden="true">
        <path d="M0 120 C 60 80, 120 40, 180 0 L 150 0 C 100 35, 50 70, 0 95 Z" fill="var(--sky-soft)"/>
      </svg>
      <div class="brand-name">Herd Sure</div>
      <h1 class="headline">
        <span class="line blue">Affordable</span>
        <span class="line blue">Diagnostics</span>
        <span class="for-row"><span class="script">for</span><span class="line green">Healthy</span></span>
        <span class="line green indent">Herds</span>
      </h1>
      <p class="subline">Herd Sure Rapid Test<br>For Livestock</p>
      <div class="hero-photo" role="img" aria-label="Photo of a brown cow with a pale calf standing beside her"></div>
    </section>

    <section class="panel brand-panel">
      <div class="brand-mark">Herd Sure</div>
    </section>

    <section class="panel features">
      <h2 class="title">Herd Sure<br>Rapid Test</h2>
      <p class="point fast"><b>Fast &amp; Efficient:</b> Rapid test results in less than 10 minutes from prep to completion</p>
      <p class="point reliable"><b>Reliable &amp; Simple:</b>Stable test performance with 2~3,Easy to operate,noprofessional skills required.</p>
      <div class="goat-photo" role="img" aria-label="Photo of a young white goat kid"></div>
      <div class="value-card">
        <div class="value-title">Affordable:</div>
        <p class="value-text">Colloidal gold-based rapid tests that combine high accuracy with cost effectiveness.</p>
        <div class="value-brand">Herd Sure</div>
      </div>
    </section>

    <section class="panel info">
      <div class="label">
        <div class="label-name">HERD SURE™</div>
        <div>Manufactured by AGRIVANTA</div>
        <div>Storage: 2-30c,Do not freeze</div>
        <div>See the instructions for</div>
      </div>
    </section>
  </main>
</body>
</html>
```